Heaven, Spare Me From Wedding Caldor

I need a book cover to be designed for a book I am writing about marrying the wrong man. I need the cover to be very eye-catching with an emotional, sympathetic and compassionate feel. Gold can be used along with any other colours . I want a very feminine feel to the book cover. I don't mind a cartoon design but must be elegant,
Let me give you a hint about Caldor, he is a very wealthy man, good looking a narcissist, a high flyer jet-setter, very very mean with his money. Really know how to pull the girls but treat them badly, he is the kind of man any women would fall for. With this information create me a cover that when any women look at they can identify and will buy the book.
Target Market(s)
Female, single women, divorced women, women who are dating.
Colors
Designer to choose colors to be used in the design.
Requirements
Must have
- must have some kind of picture o to it, bold writing of the book title yet soft in appearance. Elegant, sophisticated and very expensive yet attractive. Modern in appearance very much 21st century look to it. please stay away from the church, wedding dress.
Nice to have
- Nice to have a playful cover, yet very elegant and modern.
Should not have
- The design of the book cover should not have, any church wedding dress graphics. The book size is a jpg at 300 dpi with A5 dimensions (14.8 cm wide by 21 cm high), and make sure that your text is well within the trim line - approximately 2 cm from the edge.
- This is my autobiography
- This book aims to teach you informative Guide and strategies, how to attract the right kind of man to be your husband. What you also learn is how to understand the social fundamental truth sharps the relationship the man will have with himself and the rest of the world.
- This book will uncover the 10 worst men to Marry, using the biblical character to name these bad boys, you will learn that in today's 21st century these character is still very much around.
- Things you will learn from reading this book.
- .Break the cycle of the failed relationship.
- .Understanding the fundamental truth about a man life.
- . Recognize red flags you should not ignore when dating.
- .Strategies on how to win the spiritual on singleness
- . The do's and don't of dating.
- .How to equip yourself to defeat the curse anti-marriage
- Dorenne Walcott is co-leader with her husband Marcus Walcott Beacon 700 prayer fellowship in London, England where they live with their three grown children and Ethan their energetic 13yrs old superstar. The ministry is renowned for their Deliverance services and Teaching where Dorenne teaches the word of God with deep spiritual insight. She also has a prophetic insight into dreams and vision from a biblical perspective. Beacon 700 prayer fellowship is a 24 hours prayer warriors group who observe the 8 prayer watches. The ministry is known for their powerful teaching seminar as well there 72 prayer hours shut-in service,as well as their mentorship programme and master classes on singleness and marriages.
- please put the picture of my self on the back. I have uploaded

```html
<!DOCTYPE html>
<html lang="en">
<head>
<meta charset="utf-8">
<title>Lord don't let me Marry Caldor</title>
<link rel="stylesheet" href="https://fonts.googleapis.com/css2?family=Dancing+Script:wght@700&family=Caveat:wght@500&display=swap">
<style>
  :root {
    --paper: #fdfdf8;
    --wash-blue: #6fb6df;
    --wash-blue-soft: #bfe0f1;
    --wash-cream: #f6eec6;
    --gold: #d2a632;
    --title-crimson: #c8134a;
    --dedication-teal: #1f8698;
    --petal-blue: #2f6fb8;
    --petal-cream: #f2dfae;
    --leaf-green: #8fae6a;
  }
  html, body {
    margin: 0;
    padding: 0;
    overflow: hidden;
    background: var(--paper);
  }
  .cover {
    position: relative;
    width: 845px;
    height: 1200px;
    overflow: hidden;
    background:
      radial-gradient(ellipse 48% 40% at 50% 52%, var(--paper) 55%, transparent 100%),
      radial-gradient(ellipse 40% 30% at 95% 8%, var(--wash-blue) 0%, transparent 70%),
      radial-gradient(ellipse 35% 45% at 0% 45%, var(--wash-blue) 0%, transparent 70%),
      radial-gradient(ellipse 30% 40% at 100% 55%, var(--wash-blue) 0%, transparent 70%),
      radial-gradient(ellipse 45% 25% at 20% 100%, var(--wash-blue-soft) 0%, transparent 75%),
      radial-gradient(ellipse 40% 30% at 50% 0%, var(--wash-cream) 0%, transparent 75%),
      radial-gradient(ellipse 40% 30% at 0% 100%, var(--wash-cream) 0%, transparent 75%),
      var(--paper);
  }
  .frame-art {
    position: absolute;
    inset: 0;
    width: 845px;
    height: 1200px;
  }
  .title {
    position: absolute;
    left: 0;
    right: 0;
    top: 355px;
    margin: 0;
    text-align: center;
    font-family: "Dancing Script", cursive;
    font-weight: 700;
    font-size: 104px;
    line-height: 104px;
    color: var(--title-crimson);
    letter-spacing: -1px;
  }
  .title span { display: block; }
  .dedication {
    position: absolute;
    left: 58px;
    top: 1112px;
    margin: 0;
    font-family: "Caveat", cursive;
    font-weight: 500;
    font-size: 50px;
    color: var(--dedication-teal);
  }
</style>
</head>
<body>
<main class="cover">
  <svg class="frame-art" viewBox="0 0 722 1025" preserveAspectRatio="none" xmlns="http://www.w3.org/2000/svg">
    <defs>
      <radialGradient id="bloom-blue" cx="50%" cy="50%" r="50%">
        <stop offset="0%" stop-color="#1d4f96"/>
        <stop offset="100%" stop-color="#4d8fd0"/>
      </radialGradient>
      <radialGradient id="bloom-cream" cx="50%" cy="50%" r="50%">
        <stop offset="0%" stop-color="#e9c98a"/>
        <stop offset="100%" stop-color="#fbefcf"/>
      </radialGradient>
    </defs>

    <g class="gold-frame" fill="none" stroke="var(--gold)" stroke-width="2.5">
      <polyline points="0,240 228,58 722,245"/>
      <polyline points="0,200 240,72 722,195"/>
      <polyline points="0,765 372,898 722,790"/>
      <polyline points="0,828 360,880 722,830"/>
    </g>

    <g class="floral-top" role="img" aria-label="Watercolour bouquet: large blue rose with green leaves and cream blossoms, top left">
      <ellipse cx="62" cy="235" rx="24" ry="40" fill="var(--leaf-green)" opacity="0.7"/>
      <circle cx="140" cy="130" r="88" fill="url(#bloom-blue)"/>
      <circle cx="258" cy="100" r="42" fill="url(#bloom-cream)"/>
    </g>
    <g class="floral-top-right" role="img" aria-label="Watercolour cream blossom on the gold frame">
      <circle cx="452" cy="128" r="46" fill="url(#bloom-cream)"/>
    </g>

    <g class="floral-bottom" role="img" aria-label="Watercolour bouquet: cream peony, blue aster and small cream flower, bottom right">
      <circle cx="252" cy="872" r="36" fill="url(#bloom-cream)"/>
      <circle cx="405" cy="890" r="50" fill="url(#bloom-blue)"/>
      <ellipse cx="650" cy="780" rx="20" ry="60" fill="var(--leaf-green)" opacity="0.7"/>
      <ellipse cx="568" cy="895" rx="110" ry="85" fill="url(#bloom-cream)"/>
    </g>
  </svg>

  <h1 class="title">
    <span>Lord don't let</span>
    <span>me</span>
    <span>Marry Caldor</span>
  </h1>

  <p class="dedication">For Dorenne.</p>
</main>
</body>
</html>
```